A professional business to business web site for a contract agency called VONTAREX.

We need a very clean, very professional web site created for business to business. It is an informational web site with 3 pages. We are a company that offers contract employee placements into primarily the pharmaceutical industry. I have attached a file that describes the company more fully.

Hi,

I'm sorry if I wasn't clear, but I need to have the HTML pages created so I can just upload the files you give me to the web hosting site.

Please let me know if you have any questions.

Thanks for working on my project!

Hello,

I didn't put this in the description, but I would need the web site set up on the web hosting site as well.  The web hosting site is abrightkettle.  I want a copy of all the files as well.

Thanks,
Miles

Reason: I'm sorry, unexpectedly, I have been very busy and I haven't been able to devote the time necessary for this. I am extending the deadline by 10 days. Thank you for your patience. Thanks.

Reason: Hi everyone, I apologize again, but everything has been so busy here that I haven't been able to give this attention. I plan to work on this over the next few days. Thanks and sorry again, Miles.

Reason: I'm sorry this is taking longer than planned. I have been extremely busy. I have increased the budget on this project. Thanks.

Target Market(s)

Large professional corporations mainly in the pharmaceutical industry. The audience is hiring decisions makers within the companies and potential job candidates/job seekers.

Industry/Entity Type

Pharmaceutical

Font styles to use
Sans Serif

Requirements
Must have
• Must have a clean look that mimics the pharmaceutical industry web sites. VERY professional.
Nice to have
• A nice picture of professional business/pharma/technical people looking like a team. Colors are listed on the attached Word document.
Should not have
• No animation. Not too busy.

```html
<!DOCTYPE html>
<html lang="en">
<head>
<meta charset="utf-8">
<title>VONTAREX – Contract Professionals</title>
<link rel="stylesheet" href="https://fonts.googleapis.com/css2?family=Open+Sans:wght@400;600&display=swap">
<style>
:root{
  --brand-navy:#1f2a78;
  --nav-blue:#0d4a9e;
  --nav-active:#1d2670;
  --panel-blue:rgba(38,58,160,.82);
  --title-blue:#2b3486;
  --button-navy:#252f7c;
  --text-dark:#222;
  --footer-bg:#e7e7e7;
  --border:#cfcfcf;
  --white:#fff;
}
*{box-sizing:border-box;margin:0;padding:0}
html,body{width:1125px;height:1200px;overflow:hidden;background:var(--white);font-family:"Open Sans",Arial,sans-serif;color:var(--text-dark)}
.site{position:relative;width:1125px;height:1200px}

.header{position:absolute;top:0;left:0;width:100%;height:97px}
.brand{position:absolute;left:125px;top:22px;display:flex;align-items:center;gap:10px}
.brand-dot{width:26px;height:26px;border-radius:50%;background:var(--brand-navy)}
.brand-name{font-size:22px;font-weight:600;letter-spacing:5px;color:var(--brand-navy)}
.social{position:absolute;right:124px;top:58px;display:flex;gap:5px}
.social span{width:19px;height:19px;border-radius:50%;background:var(--nav-blue)}

.nav{position:absolute;top:97px;left:0;width:100%;height:48px;background:var(--nav-blue)}
.nav ul{list-style:none;position:absolute;left:121px;top:0;display:flex;height:48px}
.nav li{height:48px;line-height:48px;font-size:14px;font-weight:600;color:var(--white);text-align:center}
.nav li.active{background:var(--nav-active)}
.search{position:absolute;left:854px;top:14px;width:148px;height:19px;border-radius:10px;background:var(--white);font-size:10px;color:#aaa;line-height:19px;padding-left:13px}
.search svg{position:absolute;right:8px;top:3px}

.hero{position:absolute;top:145px;left:0;width:1125px;height:528px;background:linear-gradient(100deg,#3d7fd6 0%,#5f9fe6 40%,#9cc2ee 70%,#d9e6f3 100%)}
.hero-panel{position:absolute;left:123px;top:147px;width:456px;min-height:234px;background:var(--panel-blue);border-radius:4px;color:var(--white);padding:26px 15px 20px 12px}
.hero-panel h1{font-size:40px;font-weight:400;line-height:1.05;white-space:nowrap;letter-spacing:-.3px;margin-bottom:30px}
.hero-panel p{font-size:12.8px;line-height:21px;text-align:justify;padding:0 2px 0 3px}
.hero-arrow{position:absolute;top:238px;width:22px;height:53px;background:rgba(60,70,80,.75)}
.hero-arrow.prev{left:0}.hero-arrow.next{right:0}
.dots{position:absolute;left:537px;top:502px;display:flex;gap:5px}
.dots span{width:10px;height:10px;border-radius:50%;background:rgba(255,255,255,.5)}
.dots span.on{background:var(--white)}

.card{position:absolute;top:708px;width:432px;height:314px;border:1px solid var(--border)}
.card.client{left:123px}.card.seeking{left:571px}
.card-image{height:158px;position:relative}
.client .card-image{background:linear-gradient(135deg,#2c3e9a,#8d9ad0 55%,#3a4fae)}
.seeking .card-image{background:linear-gradient(90deg,#cfd6df,#e9edf2 50%,#b6c0cc)}
.more{position:absolute;right:0;bottom:0;width:88px;height:34px;background:var(--button-navy);color:var(--white);font-size:12.5px;font-weight:600;text-align:center;line-height:34px}
.card-body{padding:15px 19px}
.card-body h2{font-size:18px;font-weight:400;color:var(--title-blue);margin-bottom:6px}
.card-body p{font-size:11.5px;margin-bottom:5px}
.card-body ol{list-style:none}
.card-body li{font-size:11.5px;line-height:24.5px;display:flex}
.card-body li b{font-weight:400;width:32px}

.footer{position:absolute;top:1055px;left:0;width:100%;height:145px;background:var(--footer-bg)}
.contact{position:absolute;left:125px;top:28px;line-height:1}
.contact h3{font-size:14.5px;font-weight:400;margin-bottom:9px}
.contact .phone{font-size:17px;margin-bottom:8px}
.contact .line{font-size:11.5px;margin-bottom:8px}
.footer-nav{position:absolute;top:30px;left:470px;display:flex;gap:40px;list-style:none;font-size:14.5px}
.copyright{position:absolute;right:128px;top:105px;font-size:11px;color:#444}
</style>
</head>
<body>
<div class="site">
  <header class="header">
    <div class="brand"><span class="brand-dot"></span><span class="brand-name">VONTAREX</span></div>
    <div class="social" aria-label="Social links"><span></span><span></span><span></span><span></span><span></span></div>
  </header>

  <nav class="nav">
    <ul>
      <li class="active" style="width:105px">About Us</li>
      <li style="width:132px">Research</li>
      <li style="width:148px">Medicines</li>
      <li style="width:141px">Partnering</li>
      <li style="width:148px">Responsibility</li>
    </ul>
    <div class="search">Search
      <svg width="14" height="13" viewBox="0 0 14 13"><circle cx="5" cy="5" r="3.6" fill="none" stroke="#777" stroke-width="1.6"/><line x1="7.6" y1="7.6" x2="12.5" y2="11.5" stroke="#777" stroke-width="2"/></svg>
    </div>
  </nav>

  <section class="hero" role="img" aria-label="Scientist in safety goggles using a pipette in a laboratory with glassware">
    <div class="hero-panel">
      <h1>Enhancing your team</h1>
      <p>VONTAREXspecializes in offering contract professionals primarily to companies in pharmaceutical lab environments. We look for the top people and companies to work with. Whether you are looking for a position, or looking for a contractor, you have come to the right place. We work hard to put great team members together with great teams.</p>
    </div>
    <div class="hero-arrow prev"><svg width="22" height="53"><path d="M13 12 L8 26.5 L13 41" fill="none" stroke="#ccc" stroke-width="2"/></svg></div>
    <div class="hero-arrow next"><svg width="22" height="53"><path d="M9 12 L14 26.5 L9 41" fill="none" stroke="#ccc" stroke-width="2"/></svg></div>
    <div class="dots"><span></span><span class="on"></span><span></span><span></span></div>
  </section>

  <article class="card client">
    <div class="card-image" role="img" aria-label="White tablets held in a gloved hand"><span class="more">MORE</span></div>
    <div class="card-body">
      <h2>CLIENT COMPANIES</h2>
      <p>VONTAREX provides contract professionals in:</p>
      <ol>
        <li><b>a.</b>Project Management</li>
        <li><b>b.</b>Chromatography instrument and sotware training.</li>
        <li><b>c.</b>Laboratory positions</li>
      </ol>
    </div>
  </article>

  <article class="card seeking">
    <div class="card-image" role="img" aria-label="Lab technician examining a sample tube at a bench"><span class="more">MORE</span></div>
    <div class="card-body">
      <h2>SEEKING POSITIONS</h2>
      <p>VONTAREX provides contract professionals in:</p>
      <ol>
        <li><b>a.</b>Project Managers</li>
        <li><b>b.</b>Chromatography instrument and sotware training.</li>
        <li><b>c.</b>Laboratory technicians</li>
      </ol>
    </div>
  </article>

  <footer class="footer">
    <div class="contact">
      <h3>Contact Us</h3>
      <div class="phone">760-555-0187</div>
      <div class="line">contact.us@VONTAREX.com</div>
      <div class="line">1840 Harbor Crest Lane, Seaview, CA&nbsp; 90000</div>
    </div>
    <ul class="footer-nav">
      <li>About Us</li><li>Research</li><li>Medicines</li><li>Partnering</li><li>Responsibility</li>
    </ul>
    <div class="copyright">Copyright ©2014. All rights reserved.</div>
  </footer>
</div>
</body>
</html>
```